New Years Eve Flyer for Tavura Bay Lodge-KIMBE

Theme for New Years is PEACE, LOVE, HUMANITY.
We are in the Tropical part of the world so would like tropical look with palm trees, hibiscus flowers and fire works.
Want a picture of a masculine angel somewhere to represent my brother that passed on this year. His initials in angelic text somewhere.

Should have all my must have on the flyer all the must haves on my list.

I have attached some flyer that I like and on the night we will be giving out caps with Love peace and harmony on it.

Tavura Bay Lodge

Target Market(s)

Young target 20-35

Industry/Entity Type

Hotel

Font styles to use
Serif
Sans Serif

Colors
fabb94
ec1f27
b768aa
fbf289
fbee3f
f04a50
33a6d7
3176b5
9bcb3c

Requirements
Must have
• Tropical feel with coconout trees and hibiscus but also funky.
• Name of singers: Gerald Moku-E five
• Losana Tiveta, Bix, DJ Verumo.
• Theme :Peace, Love, Harmony and the love of Music
• Date : Saturday 31st December
• Gate Closes: Gate closes at 10pm until the New Year
• K 80.00 per person.
• NO TICKETS SOLD AT THE GATE- TICKETS SOLD FROM RECEPTION
• NO TICKET NO ENTRY
• DRESS CODE: DRESSED UP. Tropical Formal.- no shorts, collared shirts.
Nice to have
• The initials of PWT somewhere on the Angel,
• Bright colours and funky
Should not have
• No picture of sexy women,
• must be tasteful modern

```html
<!DOCTYPE html>
<html lang="en">
<head>
<meta charset="utf-8">
<title>Tavura Bay Lodge – New Years Eve Celebration</title>
<link rel="stylesheet" href="https://fonts.googleapis.com/css2?family=Oswald:wght@300;400;500;600&display=swap">
<style>
  :root {
    --sky-top: #f4f2e6;
    --sky-mid: #d3e9d8;
    --sea: #9fd1c0;
    --sea-deep: #4fa597;
    --ink-green: #2f6b35;
    --title-green: #2c6632;
    --muted-initials: #6b8c78;
    --band: #ffffff;
    --page: #ecebe7;
  }
  * { margin: 0; padding: 0; box-sizing: border-box; }
  html, body { width: 860px; height: 1200px; overflow: hidden; background: var(--page); }
  .flyer {
    position: relative;
    width: 860px;
    height: 1200px;
    overflow: hidden;
    background: linear-gradient(180deg, var(--sky-top) 0%, var(--sky-top) 24%, var(--sky-mid) 44%, var(--sea) 72%, var(--sea-deep) 100%);
    font-family: "Oswald", sans-serif;
    color: var(--ink-green);
    text-align: center;
  }
  .art { position: absolute; inset: 0; width: 860px; height: 1200px; }
  .copy { position: absolute; left: 0; width: 860px; text-transform: uppercase; }

  .venue { top: 232px; font-weight: 300; font-size: 36px; letter-spacing: 3.4px; }
  .presents { top: 284px; font-weight: 300; font-size: 21px; letter-spacing: 5px; }
  .title { top: 318px; font-weight: 600; font-size: 70px; letter-spacing: 5px; color: var(--title-green); line-height: 1.2; }
  .subtitle { top: 394px; font-weight: 400; font-size: 48px; letter-spacing: 3.4px; color: var(--title-green); line-height: 1.2; }
  .message { top: 460px; font-weight: 300; font-size: 18px; line-height: 24.5px; letter-spacing: 1px; }
  .invite { top: 563px; font-weight: 300; font-size: 17px; line-height: 30px; letter-spacing: 0.6px; }
  .gate { top: 640px; font-weight: 500; font-size: 27px; letter-spacing: 0.4px; }
  .details { top: 676px; font-weight: 400; font-size: 18px; letter-spacing: 0.8px; }
  .lineup-heading { top: 719px; font-weight: 300; font-size: 28px; letter-spacing: 2px; }
  .lineup { top: 757px; font-weight: 300; font-size: 26px; line-height: 31.5px; letter-spacing: 1.5px; list-style: none; }

  .memorial-initials {
    position: absolute; left: 718px; top: 526px;
    font-weight: 300; font-size: 26px;
    color: var(--muted-initials); letter-spacing: 1px;
  }

  .ticket-band {
    position: absolute; left: 0; top: 1050px; width: 860px; height: 77px;
    background: var(--band);
    text-transform: uppercase; color: var(--ink-green);
  }
  .ticket-rule { position: absolute; top: 10px; width: 100%; font-weight: 600; font-size: 26px; letter-spacing: 0.6px; }
  .ticket-contact { position: absolute; top: 45px; width: 100%; font-weight: 500; font-size: 19px; letter-spacing: 0.3px; }
</style>
</head>
<body>
<main class="flyer">
  <svg class="art" viewBox="0 0 860 1200">
    <defs>
      <linearGradient id="palmGrad" x1="0" y1="0" x2="0" y2="1">
        <stop offset="0" stop-color="#4b8444"/>
        <stop offset="1" stop-color="#78a668"/>
      </linearGradient>
      <linearGradient id="leafGrad" x1="0" y1="0" x2="0" y2="1">
        <stop offset="0" stop-color="#3a9444"/>
        <stop offset="1" stop-color="#22702e"/>
      </linearGradient>
      <linearGradient id="flowerGrad" x1="0" y1="0" x2="1" y2="0">
        <stop offset="0" stop-color="#f3dfe2"/>
        <stop offset="0.45" stop-color="#f1d3da"/>
        <stop offset="0.6" stop-color="#ea6c98"/>
        <stop offset="1" stop-color="#e8487f"/>
      </linearGradient>
      <linearGradient id="plumeriaGrad" x1="0" y1="0" x2="0" y2="1">
        <stop offset="0" stop-color="#fbeff0"/>
        <stop offset="1" stop-color="#f4d6da"/>
      </linearGradient>
      <linearGradient id="angelGrad" x1="0" y1="0" x2="0" y2="1">
        <stop offset="0" stop-color="#9fb3a8" stop-opacity="0.5"/>
        <stop offset="1" stop-color="#9fb3a8" stop-opacity="0.15"/>
      </linearGradient>
    </defs>

    <path role="img" aria-label="Palm fronds arching over the top and down both sides"
          fill="url(#palmGrad)" opacity="0.92"
          d="M0 0 H860 V480 C840 420 820 330 790 260 C740 150 640 95 520 85 C420 78 320 95 250 160 C200 215 175 330 150 430 C120 560 70 640 0 690 Z"/>

    <g role="img" aria-label="Banana leaves framing the lower corners">
      <path fill="url(#leafGrad)" d="M0 660 C110 690 210 790 280 960 L290 1050 H0 Z"/>
      <path fill="url(#leafGrad)" d="M860 580 C770 640 690 760 650 960 L640 1050 H860 Z"/>
    </g>

    <rect role="img" aria-label="Winged angel sketch in memory of a loved one"
          x="657" y="421" width="170" height="100" rx="6" fill="url(#angelGrad)"/>

    <path role="img" aria-label="Pale pink plumeria flowers on the right"
          fill="url(#plumeriaGrad)"
          d="M860 700 C800 705 765 750 770 800 C775 860 790 920 800 980 L860 990 Z"/>

    <path role="img" aria-label="White and pink hibiscus blossoms along the bottom"
          fill="url(#flowerGrad)"
          d="M0 805 C80 790 170 830 230 880 C290 860 380 880 430 930 C480 890 560 880 620 910 C690 890 780 900 860 950 V1200 H0 Z"/>
  </svg>

  <p class="copy venue">Tavura Bay Lodge</p>
  <p class="copy presents">Presents</p>
  <h1 class="copy title">New Years Eve</h1>
  <h2 class="copy subtitle">Celebration</h2>

  <p class="copy message">
    The world all the craziness happening in the world,<br>
    we want to celebrate all the positive.<br>
    This year Tavura wants to promote love, peace and humanity<br>
    and celebrate this as our New Years Eve 2016 theme.
  </p>
  <p class="copy invite">Come and join in the fun.<br>Giveaways on entry</p>

  <p class="copy gate">Gate shuts @ 10 PM till the New Year</p>
  <p class="copy details">Saturday 31st December | Dress: Tropical Formal | K 80.00 per ticket</p>

  <p class="copy lineup-heading">Entertainment:</p>
  <ul class="copy lineup">
    <li>DJ Verumo</li>
    <li>Gerald Moku- E-Five</li>
    <li>Losana Tiveta</li>
    <li>Bix</li>
  </ul>

  <span class="memorial-initials">PWT</span>

  <section class="ticket-band">
    <p class="ticket-rule">No tickets sold at the gate- ticket by entry only</p>
    <p class="ticket-contact">Tickets sold at the Tavura reception. 70420685- reservations@tavurabaylodge.com</p>
  </section>
</main>
</body>
</html>
```